Design a nice single page website containing a link list

Hello,

you should design a nice single page website to replace the old website http://www.tovrella.de/

The company is running multiple flag shops. Your new website should only lead to a lot of other company websites. They are mentioned below. No link dropdowns please. We would like to see all links.

The company is offering flags. Big flags, but the special products are high quality diplomatic car flags. It is important, that people see, that it is about flags and specialy about car flags.

As customers are very international, the website should not contain unnecessary text. No text, no wrong languages.

You should implement links to:

Car Flag Shops: (pleaae don't use this as headline. Use symbols)
New Logo: Little car attached (without text below)
http://www.ridepennon.eu (english site payment in Euro)
http://us.ridepennon.eu (english site payment in USD)
http://fr.ridepennon.eu (french site payment in Euro)
http://es.ridepennon.eu (spanish site payment in Euro)
http://de.ridepennon.eu (germansite payment in Euro)

http://www.ridepennon.net (english site payment in USD)
http://www.ridepennant.co.uk (english site payment in british pounds)
http://www.wagen-wimpel.net (german site payment in Euro)
http://www.wagen-banner.at (austrian site payment in Euro)
http://www.wagen-wimpl.ch (german site payment in Swiss Franken)

Big flag shops: (pleaae don't use this as headline. Use symbols)
Logo: tovRella (attached incl. font) (black part of logo can also be made white)
(World map used next to the tovRella font attached)
http://www.tovrella.ne/ (english site payment in Euro)
http://fr.tovrella.net (french site payment in Euro)
http://es.tovrella.net (spanish site payment in Euro)
http://de.tovrella.net (german site payment in Euro)
http://it.tovrella.net (italian site payment in Euro)

Car flags product page: (pleaae don't use this as headline. Use symbols)
Logo: EnvoyPennon (attached incl. font)
http://www.envoy-pennon.com (english site)
http://fr.envoy-pennon.com (french site)
http://es.envoy-pennon.com (spanish site)
http://de.envoy-pennon.com (german site)

Please also add links to
English Blog
German Blog
4 language newsletter registration forms.

Also company data has to be added to the bottom of the page.
You could copy / paste from here:
http://www.ridepennon.eu/tovRella-GmbH

No additional links. No social icons.

General design:
Customers are, ambassoders, embassies, international organisiations.
Customers are powerful men, who want to show their power.
That's the reason, why they add this car flags to their car.

So colors should not be too soft. In the past we used colors like black and gold.
Completly black / dark background and bright white text is ok.

Most of our company prints have the kelvane arch in the background.
It would be good to include this also. (Image attached)

It is about a flag company. So don't forget to add big flags.
It would be also good to include an image like this:
http://de.pixvendra.com/id/38275016

Logos are available in high resolution. At the end you should mail us psd file with your winning design.

Please feel free to use all images you will find on the websites above.
If you need special images, please let me know, and we willt try to provide them.

Kind regards,

Dorian
Updates

Hello,
thanks for your feedback.Project payment is now committed.
Kind regards,
Lorenzo

Target Market(s)

World wide

Industry/Entity Type

Flag

Requirements
Must have
• Self explaining links to all the target pages.
Should not have
• unnecessary text. Domain names and logos with text are fine.
I think, we could avoid nearly all other text.

```html
<!DOCTYPE html>
<html lang="en">
<head>
<meta charset="utf-8">
<title>tovRella – Flag Shops</title>
<link rel="stylesheet" href="https://fonts.googleapis.com/css2?family=Questrial&display=swap">
<style>
  :root{
    --page:#ffffff;
    --ink:#1a1a1a;
    --gold:#a8842c;
    --rule-bar:#555555;
    --rule:#222222;
    --stage:#000000;
    --uk-blue:#012169;
    --uk-red:#c8102e;
    --de-red:#dd0000;
    --de-gold:#ffce00;
    --fr-blue:#0055a4;
    --fr-red:#ef4135;
    --es-red:#aa151b;
    --es-gold:#f1bf00;
    --at-red:#ed2939;
  }
  *{box-sizing:border-box;margin:0;padding:0}
  html,body{width:1200px;height:801px;overflow:hidden;background:var(--page)}
  body{position:relative;font-family:"Questrial",sans-serif;color:var(--ink)}
  .flag{width:27px;height:18px;vertical-align:middle;display:inline-block}
  .site-header .brand{position:absolute;left:80px;top:36px;font-size:42px;font-weight:400;color:var(--ink);letter-spacing:1px}
  .site-nav{position:absolute;top:55px;left:756px;display:flex;align-items:center;font-size:14px;letter-spacing:1px}
  .site-nav .group{display:flex;align-items:center;gap:9px}
  .site-nav .group + .group{margin-left:30px}
  .site-nav .flag{width:28px;height:19px}
  .bar{position:absolute;left:0;top:92px;width:1200px;height:8px;background:var(--rule-bar)}
  .hero{position:absolute;left:0;top:100px;width:1200px;height:335px;background:var(--stage)}
  .hero .arch{position:absolute;left:215px;top:0;width:778px;height:335px;
    background:radial-gradient(ellipse 40% 55% at 68% 62%,#e0b068 0%,#a07434 35%,transparent 75%),
    radial-gradient(ellipse 20% 40% at 15% 70%,#b88a48 0%,transparent 80%),
    linear-gradient(180deg,#0b1f8a 0%,#142a9a 45%,#0a0f3a 82%,#050508 100%);
    -webkit-mask-image:linear-gradient(90deg,transparent 0,#000 6%,#000 90%,transparent 100%);
    mask-image:linear-gradient(90deg,transparent 0,#000 6%,#000 90%,transparent 100%)}
  .shops{position:absolute;top:470px;left:0;width:1200px}
  .shop-mark{position:absolute;top:0;height:52px;display:flex;align-items:center;font-size:28px;color:var(--ink)}
  .shop-mark.gold{color:var(--gold)}
  .shop-mark .dot{width:12px;height:12px;border-radius:50%;background:var(--ink);margin-right:10px}
  .link-list{position:absolute;top:62px;list-style:none;font-size:11px;letter-spacing:.2px}
  .link-list li{height:26.4px;display:flex;align-items:center;white-space:nowrap}
  .link-list a{color:var(--ink);text-decoration:none}
  .link-list .flag{margin:0 4px 0 3px}
  .footer-rule{position:absolute;left:76px;top:699px;width:1048px;height:1px;background:var(--rule)}
  .site-footer{position:absolute;top:715px;left:0;width:1200px;font-size:11px;line-height:15.3px;letter-spacing:.5px}
  .site-footer address{position:absolute;font-style:normal}
</style>
</head>
<body>
<svg width="0" height="0" style="position:absolute">
  <defs>
    <symbol id="f-uk" viewBox="0 0 60 40" preserveAspectRatio="none">
      <rect width="60" height="40" fill="var(--uk-blue)"/>
      <path d="M0 0L60 40M60 0L0 40" stroke="#fff" stroke-width="8"/>
      <path d="M0 0L60 40M60 0L0 40" stroke="var(--uk-red)" stroke-width="3"/>
      <path d="M30 0V40M0 20H60" stroke="#fff" stroke-width="12"/>
      <path d="M30 0V40M0 20H60" stroke="var(--uk-red)" stroke-width="7"/>
    </symbol>
    <symbol id="f-de" viewBox="0 0 3 3" preserveAspectRatio="none">
      <rect width="3" height="1" fill="#000"/><rect y="1" width="3" height="1" fill="var(--de-red)"/><rect y="2" width="3" height="1" fill="var(--de-gold)"/>
    </symbol>
    <symbol id="f-fr" viewBox="0 0 3 3" preserveAspectRatio="none">
      <rect width="1" height="3" fill="var(--fr-blue)"/><rect x="1" width="1" height="3" fill="#fff"/><rect x="2" width="1" height="3" fill="var(--fr-red)"/>
    </symbol>
    <symbol id="f-es" viewBox="0 0 4 4" preserveAspectRatio="none">
      <rect width="4" height="4" fill="var(--es-red)"/><rect y="1" width="4" height="2" fill="var(--es-gold)"/>
    </symbol>
    <symbol id="f-it" viewBox="0 0 3 3" preserveAspectRatio="none">
      <rect width="1" height="3" fill="#009246"/><rect x="1" width="1" height="3" fill="#fff"/><rect x="2" width="1" height="3" fill="#ce2b37"/>
    </symbol>
    <symbol id="f-at" viewBox="0 0 3 3" preserveAspectRatio="none">
      <rect width="3" height="3" fill="var(--at-red)"/><rect y="1" width="3" height="1" fill="#fff"/>
    </symbol>
  </defs>
</svg>

<header class="site-header">
  <div class="brand">tovRella</div>
  <nav class="site-nav">
    <div class="group">Blog
      <a href="#"><svg class="flag"><use href="#f-uk"/></svg></a>
      <a href="#"><svg class="flag"><use href="#f-de"/></svg></a>
    </div>
    <div class="group">Newsletter
      <a href="#"><svg class="flag"><use href="#f-uk"/></svg></a>
      <a href="#"><svg class="flag"><use href="#f-de"/></svg></a>
      <a href="#"><svg class="flag"><use href="#f-fr"/></svg></a>
      <a href="#"><svg class="flag"><use href="#f-es"/></svg></a>
    </div>
  </nav>
</header>

<div class="bar"></div>
<section class="hero">
  <div class="arch" role="img" aria-label="Kelvane arch illuminated at night under a deep blue sky"></div>
</section>

<main class="shops">
  <div class="shop-mark" style="left:105px"><span class="dot"></span>tovRella</div>
  <div class="shop-mark gold" style="left:366px">EnvoyPennon</div>
  <div class="shop-mark" style="left:648px">RidePennon</div>

  <ul class="link-list big-flag-shops" style="left:99px">
    <li><a href="#">http://www.tovrella.ne/ (</a><svg class="flag"><use href="#f-uk"/></svg>Euro)</li>
    <li><a href="#">http://fr.tovrella.net (</a><svg class="flag"><use href="#f-fr"/></svg>Euro)</li>
    <li><a href="#">http://es.tovrella.net (</a><svg class="flag"><use href="#f-es"/></svg>Euro)</li>
    <li><a href="#">http://de.tovrella.net (</a><svg class="flag"><use href="#f-de"/></svg>Euro)</li>
    <li><a href="#">http://it.tovrella.net (</a><svg class="flag"><use href="#f-it"/></svg>Euro)</li>
  </ul>
  <ul class="link-list envoy-pages" style="left:355px">
    <li><a href="#">http://www.envoy-pennon.com (</a><svg class="flag"><use href="#f-uk"/></svg>)</li>
    <li><a href="#">http://fr.envoy-pennon.com (</a><svg class="flag"><use href="#f-fr"/></svg>)</li>
    <li><a href="#">http://es.envoy-pennon.com (</a><svg class="flag"><use href="#f-es"/></svg>)</li>
    <li><a href="#">http://de.envoy-pennon.com (</a><svg class="flag"><use href="#f-de"/></svg>)</li>
  </ul>
  <ul class="link-list car-flag-shops" style="left:627px">
    <li><a href="#">http://www.ridepennon.eu (</a><svg class="flag"><use href="#f-uk"/></svg>Euro)</li>
    <li><a href="#">http://us.ridepennon.eu (</a><svg class="flag"><use href="#f-uk"/></svg>USD)</li>
    <li><a href="#">http://fr.ridepennon.eu (</a><svg class="flag"><use href="#f-fr"/></svg>Euro)</li>
    <li><a href="#">http://es.ridepennon.eu (</a><svg class="flag"><use href="#f-es"/></svg>Euro)</li>
    <li><a href="#">http://de.ridepennon.eu (</a><svg class="flag"><use href="#f-de"/></svg>Euro)</li>
  </ul>
  <ul class="link-list car-flag-shops" style="left:883px">
    <li><a href="#">http://www.ridepennon.net/ (</a><svg class="flag"><use href="#f-uk"/></svg>USD)</li>
    <li><a href="#">http://www.ridepennant.co.uk (</a><svg class="flag"><use href="#f-uk"/></svg>british pounds)</li>
    <li><a href="#">http://www.wagen-wimpel.net (</a><svg class="flag"><use href="#f-de"/></svg>Euro)</li>
    <li><a href="#">http://www.wagen-banner.at (</a><svg class="flag"><use href="#f-at"/></svg>Euro)</li>
    <li><a href="#">http://www.wagen-wimpl.ch (</a><svg class="flag"><use href="#f-de"/></svg>Swiss Franken)</li>
  </ul>
</main>

<div class="footer-rule"></div>
<footer class="site-footer">
  <address style="left:191px">tovRella GmbH<br>Am Lindenhang 14/3<br>71549 Aldersbrunn<br>Germany</address>
  <address style="left:453px">Tel: +49 (0) 711 - 48 27 19 340<br>Fax: +49 (0) 711 - 48 27 19 349<br>Mail: info@tovrella.de</address>
  <address style="left:715px">CEO, Geschäftsführer: Lorenzo Varnholt<br>Handelsregister: HRB 615093, Amtsgericht Stuttgart<br>Ust.-ID: DE902366418</address>
</footer>
</body>
</html>
```